International wholesale business needs a business card

We need a business card.

Company Details:
Company Name and logo
Address, Phone number, Website
Employee Details:
Name, Designation, Mobile Number & Email address

```html
<!DOCTYPE html>
<html lang="en">
<head>
<meta charset="UTF-8">
<title>Veranta Trading – Business Card</title>
<link href="https://fonts.googleapis.com/css2?family=Libre+Baskerville:wght@700&family=Open+Sans:wght@400;600&display=swap" rel="stylesheet">
<style>
  :root {
    --bg: #5b5b5e;
    --card: #ffffff;
    --red: #c1272d;
    --grey: #8e9296;
    --ink: #3d3f42;
  }
  * { box-sizing: border-box; margin: 0; padding: 0; }
  html, body { width: 1200px; height: 1095px; overflow: hidden; }
  body {
    background: var(--bg);
    font-family: "Open Sans", sans-serif;
    position: relative;
  }
  .card {
    position: absolute;
    left: 180px;
    width: 840px;
    height: 480px;
    background: var(--card);
    border-radius: 22px;
    box-shadow: 0 10px 30px rgba(0,0,0,0.35);
  }
  .card--front { top: 45px; }
  .card--back { top: 570px; }

  .brand {
    position: absolute;
    display: flex;
    align-items: center;
    gap: 18px;
  }
  .brand__mark {
    width: 20px; height: 20px;
    background: var(--grey);
    flex: none;
  }
  .brand__name {
    font-family: "Libre Baskerville", serif;
    font-weight: 700;
    color: var(--red);
    letter-spacing: 1px;
    line-height: 1;
    white-space: nowrap;
  }
  .card--front .brand { left: 50%; top: 50%; transform: translate(-50%, -50%); }
  .card--front .brand__name { font-size: 44px; }
  .card--back .brand { left: 80px; top: 236px; gap: 14px; }
  .card--back .brand__mark { width: 14px; height: 14px; }
  .card--back .brand__name { font-size: 25px; }

  .divider { position: absolute; left: 470px; width: 3px; }
  .divider--top { top: 110px; height: 70px; background: var(--grey); }
  .divider--mid { top: 192px; height: 110px; background: var(--red); width: 4px; }
  .divider--low { top: 314px; height: 64px; background: var(--grey); }

  .details { position: absolute; left: 500px; top: 100px; }
  .details__name {
    font-family: "Libre Baskerville", serif;
    font-weight: 700;
    font-size: 30px;
    color: var(--red);
    letter-spacing: 0.5px;
  }
  .details__title { font-size: 19px; color: var(--ink); margin-top: 4px; }
  .details__address { font-size: 18px; color: var(--red); margin-top: 18px; line-height: 1.45; }
  .contact { list-style: none; margin-top: 14px; }
  .contact__item {
    display: flex; align-items: center; gap: 12px;
    font-size: 18px; color: var(--ink); line-height: 1.75;
  }
  .contact__icon { width: 16px; height: 16px; fill: var(--red); flex: none; }
</style>
</head>
<body>
  <section class="card card--front">
    <div class="brand">
      <span class="brand__mark"></span>
      <span class="brand__name">VERANTA TRADING</span>
    </div>
  </section>

  <section class="card card--back">
    <div class="brand">
      <span class="brand__mark"></span>
      <span class="brand__name">VERANTA TRADING</span>
    </div>

    <span class="divider divider--top"></span>
    <span class="divider divider--mid"></span>
    <span class="divider divider--low"></span>

    <div class="details">
      <p class="details__name">ROHAN MEHTA</p>
      <p class="details__title">President</p>
      <p class="details__address">2750 Linden Park Road Suite 400<br>Fairview Heights, MD 2087</p>
      <ul class="contact">
        <li class="contact__item">
          <svg class="contact__icon" viewBox="0 0 24 24"><path d="M6.6 10.8a15.1 15.1 0 0 0 6.6 6.6l2.2-2.2a1 1 0 0 1 1-.25 11.4 11.4 0 0 0 3.6.57 1 1 0 0 1 1 1V20a1 1 0 0 1-1 1A17 17 0 0 1 3 4a1 1 0 0 1 1-1h3.5a1 1 0 0 1 1 1c0 1.25.2 2.45.57 3.57a1 1 0 0 1-.25 1z"/></svg>
          (410) 555-0148
        </li>
        <li class="contact__item">
          <svg class="contact__icon" viewBox="0 0 24 24"><path d="M2 5h20v2l-10 6L2 7z"/><path d="M2 9l10 6 10-6v10H2z"/></svg>
          dlane@verantatrading.com
        </li>
        <li class="contact__item">
          <svg class="contact__icon" viewBox="0 0 24 24"><path d="M12 2a10 10 0 1 0 0 20 10 10 0 0 0 0-20zm6.9 6h-3a15 15 0 0 0-1.3-3.9A8 8 0 0 1 18.9 8zM12 4a13 13 0 0 1 1.9 4h-3.8A13 13 0 0 1 12 4zM4.3 14a8 8 0 0 1 0-4h3.4a16 16 0 0 0 0 4zm.8 2h3a15 15 0 0 0 1.3 3.9A8 8 0 0 1 5.1 16zm3-8h-3a8 8 0 0 1 4.3-3.9A15 15 0 0 0 8.1 8zM12 20a13 13 0 0 1-1.9-4h3.8A13 13 0 0 1 12 20zm2.3-6H9.7a14 14 0 0 1 0-4h4.6a14 14 0 0 1 0 4zm.3 5.9a15 15 0 0 0 1.3-3.9h3a8 8 0 0 1-4.3 3.9zm1.7-5.9a16 16 0 0 0 0-4h3.4a8 8 0 0 1 0 4z"/></svg>
          www.verantatrading.com
        </li>
      </ul>
    </div>
  </section>
</body>
</html>
```